Original catchy book cover

I need a book cover for my book "The Steady Harbor Manual" (https://quillpress.example/harbormanual). This will be a book self published on brightmart.
The book talks about the following concepts:
- Iterative product delivery
- Early discovery using feedback from customers
- Start small, think big, move fast
- Slice the product into valuable increments that can be validated with customers
- Experimental approach to deciding the next slice of work
A simple cover that stands out from the business books already out there! Some examples are:
https://www.brightmart.example/Field-Notes-Thriving-Teams-Steadily-ebook/dp/Q00XTR4KWZ/ref=sr_1_1?ie=UTF8&qid=1500000001&sr=8-1&keywords=field+notes
https://www.brightmart.example/Quiet-Harbor-Almanac-Shape-Offerings-ebook/dp/Q00MVK219J/ref=sr_1_1?s=digital-text&ie=UTF8&qid=1500000002&sr=1-1&keywords=quiet+harbor+almanac
https://www.brightmart.example/Course-Charts-Renewed-Heading-Fog-ebook/dp/Q099WT71ZD/ref=pd_sim_351_2?_encoding=UTF8&psc=1&refRID=9QZTRWJDDAV52LM0NKPP
Lastly, attached are 2 draft covers that i've been playing with. Would love a graphic as part of the cover if it makes sense in your design! The graphic should tie to the meaning or themes of the book. Emphasis on ways of working, collaboration, experimentation, hypothesis, agile, incremental or adaptive. Those are some words that describe the content of the book.
Alternatively, something abstract could also be an option if a literal graphic doesn't suit the theme of your design.
Target Market(s)
Product owners, scrum masters, people in the agile community, software developers, designers
Industry/Entity Type
Information Technology
Font styles to use
Colors
Designer to choose colors to be used in the design.
Requirements
Must have
- Title, Subtitle, Author Name
- Back of the book should have space for a description (use lorem ipsum for now)
- Please use the editorial logo
- (please omit "created by Tomas Verlindt" because the editorial logo replaces that.
- The design must be original art or graphics (i.e. it should be similar to another cover in this topic).
Nice to have
- A graphic would be ideal if it is relevant to the book topic, otherwise a nice simple cover that uses colors or patterns that are easy to recall.
- The color suggestions below are suggestions only. Do not feel you have to incorporate all the colors and feel free to recommend an alternate palette.
Should not have
- Clipart or generic stock art photos. Images for the sake of images, traditional logos (e.g. a computer, a phone etc unless it's part of an overall theme that ties the logos together).

```html
<!DOCTYPE html>
<html lang="en">
<head>
<meta charset="utf-8">
<title>The Steady Harbor Manual — Cover Wrap</title>
<link rel="stylesheet" href="https://fonts.googleapis.com/css2?family=Montserrat:wght@600;700&family=Questrial&family=Source+Sans+3:wght@400&family=Open+Sans:wght@400&display=swap">
<style>
  :root {
    --stage: #1c1c1c;
    --green: #00c266;
    --teal: #08b4a8;
    --blue: #0a98fb;
    --white: #ffffff;
    --yellow: #fff23a;
    --art-glow: rgba(243, 236, 74, .42);
    --art-fade: rgba(217, 232, 90, .12);
  }
  * { box-sizing: border-box; margin: 0; padding: 0; }
  html, body { width: 1200px; height: 670px; overflow: hidden; background: var(--stage); }
  .cover-wrap {
    position: absolute; left: 102px; top: 0; width: 996px; height: 670px; overflow: hidden;
    background: linear-gradient(180deg, var(--green) 0%, var(--teal) 45%, var(--blue) 100%);
    color: var(--white);
  }
  .panel { position: absolute; top: 0; height: 670px; overflow: hidden; }
  .back { left: 0; width: 454px; }
  .spine { left: 454px; width: 90px; border-left: 1px solid rgba(255,255,255,.12); border-right: 1px solid rgba(255,255,255,.12); }
  .front { left: 544px; width: 452px; }

  .title { position: absolute; text-align: center; font-family: "Montserrat", sans-serif; font-weight: 700; line-height: .95; }
  .title-kicker { display: block; font-family: "Questrial", sans-serif; font-weight: 400; letter-spacing: .16em; }
  .title-main { display: block; letter-spacing: -.01em; }

  .back .title { left: 0; width: 454px; top: 36px; }
  .back .title-kicker { font-size: 22px; margin-bottom: 4px; }
  .back .title-main { font-size: 46px; }

  .blurb {
    position: absolute; font-family: "Open Sans", sans-serif; font-size: 11.6px; line-height: 13.2px;
    text-align: justify; text-indent: 2.2em;
  }
  .back .description { left: 67px; top: 172px; width: 326px; }
  .author-heading {
    position: absolute; left: 160px; top: 420px; font-family: "Montserrat", sans-serif; font-weight: 600;
    font-size: 22px; letter-spacing: .14em;
  }
  .author-photo { position: absolute; left: 47px; top: 446px; width: 86px; height: 103px; background: var(--white); }
  .back .bio { left: 160px; top: 459px; width: 252px; }
  .imprint {
    position: absolute; display: flex; align-items: center; gap: 10px;
    font-family: "Questrial", sans-serif; font-weight: 400; color: var(--white);
  }
  .imprint-dot { border-radius: 50%; border: 3px solid var(--white); flex: none; }
  .back .imprint { left: 47px; top: 588px; font-size: 18px; line-height: 19px; }
  .back .imprint-dot { width: 54px; height: 54px; }
  .imprint small { font-size: .78em; }
  .isbn-frame { position: absolute; left: 302px; top: 582px; width: 108px; height: 68px; border: 1px solid var(--white); }

  .spine-text {
    position: absolute; writing-mode: vertical-rl; transform: rotate(180deg);
    font-family: "Montserrat", sans-serif; font-weight: 700; line-height: 1;
  }
  .spine-title { left: 22px; top: 78px; height: 270px; font-size: 24px; text-align: left; }
  .spine-author { left: 32px; top: 448px; font-size: 25px; letter-spacing: .03em; }

  .front .imprint { left: 182px; top: 18px; font-size: 13px; line-height: 13px; }
  .front .imprint-dot { width: 38px; height: 38px; }
  .front .title { left: 0; width: 452px; top: 80px; }
  .front .title-kicker { font-size: 31px; margin-bottom: 8px; }
  .front .title-main { font-size: 76px; }
  .front .title-main.accent { color: var(--yellow); }
  .subtitle {
    position: absolute; left: 0; width: 452px; top: 265px; text-align: center;
    font-family: "Source Sans 3", sans-serif; font-size: 15.5px; line-height: 16px;
  }
  .theme-art {
    position: absolute; left: 86px; top: 312px; width: 280px; height: 280px; border-radius: 50% 50% 46% 46%;
    background: radial-gradient(circle at 50% 45%, var(--art-glow), var(--art-fade) 70%, rgba(217,232,90,0) 100%);
  }
  .front .author-name {
    position: absolute; left: 0; width: 452px; top: 618px; text-align: center;
    font-family: "Montserrat", sans-serif; font-weight: 600; font-size: 25px; letter-spacing: .14em;
  }
</style>
</head>
<body>
  <main class="cover-wrap">
    <section class="panel back">
      <h2 class="title">
        <span class="title-kicker">THE STEADY</span>
        <span class="title-main">HARBOR</span>
        <span class="title-main">MANUAL</span>
      </h2>
      <div class="blurb description">
        <p>Lorem ipsum dolor sit amet, consectetur adipiscing elit. Proin molestie, eros et vehicula consequat, augue mauris porttitor orci, vel tincidunt est felis at lectus. Integer euismod molestie arcu, vitae cursus nunc faucibus vel. Donec gravida iaculis sem sit amet tincidunt. Nam placerat, lectus eu maximus faucibus, lectus lectus tincidunt lectus, ut posuere ipsum eros id nibh. Etiam laoreet, nunc ac egestas tempus, lectus ante tincidunt nunc, a laoreet ex erat vitae justo.</p>
        <p>Fusce gravida felis at semper sagittis. Fusce rutrum vel augue quis posuere. Curabitur non mi eu libero porta tempus in sed mauris. Aliquam tristique iaculis lacus, ac scelerisque odio egestas sit amet. Vestibulum dapibus gravida mi, sed semper turpis tristique maximus. Aenean viverra odio ligula, sed rhoncus ex tempus ac. Suspendisse varius dapibus pellentesque. Fusce sollicitudin mattis ipsum, eget consequat velit faucibus eu.</p>
      </div>
      <h3 class="author-heading">MARA ELLISON</h3>
      <div class="author-photo" role="img" aria-label="Author portrait placeholder"></div>
      <p class="blurb bio">Lorem ipsum dolor sit amet, consectetur adipiscing elit. Proin molestie, eros et vehicula consequat, augue mauris porttitor orci, vel tincidunt est felis at lectus. Integer euismod molestie arcu, vitae cursus nunc faucibus vel. Donec gravida iaculis sem sit amet tincidunt.</p>
      <div class="imprint">
        <span class="imprint-dot"></span>
        <span>Editora<br>Verlindt<br><small>verlindt.example</small></span>
      </div>
      <div class="isbn-frame"></div>
    </section>

    <section class="panel spine">
      <div class="spine-text spine-title">THE STEADY<br>HARBOR MANUAL</div>
      <div class="spine-text spine-author">MARA ELLISON</div>
    </section>

    <section class="panel front">
      <div class="imprint">
        <span class="imprint-dot"></span>
        <span>Editora<br>Verlindt<br><small>verlindt.example</small></span>
      </div>
      <h1 class="title">
        <span class="title-kicker">THE STEADY</span>
        <span class="title-main accent">HARBOR</span>
        <span class="title-main">MANUAL</span>
      </h1>
      <p class="subtitle">A practitioner’s guide to building viable<br>products customers love</p>
      <div class="theme-art" role="img" aria-label="Cluster of yellow line icons about product work: screen, charts, gear, lightbulb, megaphone, chat bubbles, cart and map pins"></div>
      <p class="author-name">MARA ELLISON</p>
    </section>
  </main>
</body>
</html>
```